" Atuo como clínica-geral (prevenção, raspagem e profilaxia, restauração, clareamento dental, etc.) e como especialista em endodontia (canal). Outro profissional atende no consultório na área de semiologia (diagnósticos de doenças da cavidade oral através de biópsias e exames complementares, doenças como câncer bucal, candidíase bucal etc.). E futuramente pretendo trazer um profissional de ortodontia (aparelho) para atender também no consultório. É um consultório de apenas uma sala, com intuito de atendimento com mais tranquilidade, e não em grande quantidade. Um tratamento com mais conforto para o paciente. "

```html
<!DOCTYPE html>
<html lang="pt-BR">
<head>
<meta charset="utf-8">
<title>Bellamar Odontologia — Papel timbrado</title>
<link rel="stylesheet" href="https://fonts.googleapis.com/css2?family=Cinzel:wght@500&family=Lato:wght@400&display=swap">
<style>
  :root {
    --backdrop: #ececec;
    --paper: #ffffff;
    --swoosh: #e2e2e2;
    --brand-violet: #8a78bd;
    --footer-ink: #6f6f6f;
  }
  * { margin: 0; padding: 0; box-sizing: border-box; }
  html, body {
    width: 1200px;
    height: 1200px;
    overflow: hidden;
    background: var(--backdrop);
  }
  .letterhead {
    position: absolute;
    left: 218px;
    top: 60px;
    width: 764px;
    height: 1080px;
    background: var(--paper);
    box-shadow: 0 2px 10px rgba(0, 0, 0, 0.12);
    overflow: hidden;
  }
  .letterhead__swoosh {
    position: absolute;
    inset: 0;
    width: 100%;
    height: 100%;
  }
  .brand {
    position: absolute;
    left: 36px;
    top: 34px;
    display: flex;
    align-items: center;
    gap: 12px;
    color: var(--brand-violet);
    font-family: "Cinzel", serif;
    font-weight: 500;
  }
  .brand__dot {
    width: 40px;
    height: 40px;
    border-radius: 50%;
    background: var(--brand-violet);
  }
  .brand__name {
    display: block;
    font-size: 30px;
    line-height: 1;
    letter-spacing: 0.02em;
  }
  .brand__tagline {
    display: block;
    font-size: 10px;
    letter-spacing: 0.42em;
    margin-top: 4px;
  }
  .letterhead__footer {
    position: absolute;
    left: 0;
    right: 0;
    bottom: 30px;
    text-align: center;
    font-family: "Lato", sans-serif;
    font-size: 11px;
    line-height: 1.5;
    color: var(--footer-ink);
  }
</style>
</head>
<body>
  <main class="letterhead">
    <svg class="letterhead__swoosh" viewBox="0 0 764 1080" preserveAspectRatio="none" aria-hidden="true">
      <path d="M300 0 L764 0 L764 830 C 560 700 330 330 300 0 Z" fill="var(--swoosh)"/>
    </svg>

    <header class="brand">
      <span class="brand__dot"></span>
      <span class="brand__text">
        <span class="brand__name">BELLAMAR</span>
        <span class="brand__tagline">ODONTOLOGIA</span>
      </span>
    </header>

    <footer class="letterhead__footer">
      <p class="letterhead__contact">(11) 4000-2200 | contato@bellamar.com</p>
      <p class="letterhead__address">Rua das Flores, 120 · Sala 3 · Centro · São Paulo · SP · CEP 01000-000</p>
    </footer>
  </main>
</body>
</html>
```